** Wanted ** Wordpress web design for scaffolding rental and construction company

We need a website design and must be functional to show a basic overview of what our company offers as a service. We have a domain name and a logo but we need web design. This web site should have another scaffolding rental page for construction and renovation as well as a quote section where customers can enter their personal information and also upload photos. The site% 26quot; www.brixmorvo.com% 26quot; should be intuitive, clear and classy ... The logo must be found on the site in several ways.

Target Market(s)

Professional and no professional

Coding

Coded - Design and coding required

Number of Pages Required

3 page

Font styles to use
Serif
Sans Serif
Decorative
Script

Requirements
Must have
• Our logo
Nice to have
• Slogan:% 26quot; The height% 26 # 224; port% 26 # 233; e hand% 26quot;

```html
<!DOCTYPE html>
<html lang="en">
<head>
<meta charset="utf-8">
<title>Brixmorvo – Scaffolding Rental &amp; Construction</title>
<link href="https://fonts.googleapis.com/css2?family=Bungee&family=Source+Sans+3:ital,wght@0,400;0,600;0,700;1,400&display=swap" rel="stylesheet">
<style>
:root{
  --blue:#0a9de0;
  --panel:#e5f4fb;
  --ink:#111418;
  --text:#5d6269;
  --line:#e3e6ea;
  --dark:#0d0f12;
  --white:#ffffff;
}
*{box-sizing:border-box;margin:0;padding:0}
html,body{width:1200px;height:4246px;overflow:hidden}
body{position:relative;background:var(--white);font-family:"Source Sans 3",Arial,sans-serif;color:var(--text)}
.abs{position:absolute}
.display{font-family:"Bungee",Impact,sans-serif;color:var(--ink);font-weight:400;letter-spacing:.5px}
.btn{position:absolute;background:var(--blue);color:var(--white);font-family:"Bungee",Impact,sans-serif;display:flex;align-items:center;justify-content:center;font-size:13px;letter-spacing:.3px}
.photo{position:absolute}
.small{font-size:10.5px;line-height:20px;color:var(--text)}
.center{text-align:center}

/* header */
.top-rule{top:0;left:0;width:1200px;height:3px;background:var(--blue)}
.brand{display:flex;align-items:center;gap:8px;font-family:"Source Sans 3",Arial,sans-serif;font-weight:700;color:var(--blue);letter-spacing:1px}
.brand .mark{width:14px;height:14px;background:var(--blue)}
.header-brand{left:163px;top:30px;font-size:24px}
.nav{display:flex;gap:22px;font-size:11.5px;color:#666}
.header-nav{left:455px;top:40px}
.quote-btn{left:900px;top:28px;width:150px;height:42px}

/* hero */
.hero{left:38px;top:97px;width:1137px;height:638px;background:linear-gradient(180deg,#1b2531 0%,#233140 45%,#35402a 80%,#26301e 100%)}
.hero-shade{left:38px;top:97px;width:1137px;height:638px;background:rgba(0,0,0,.35)}
.hero-title{left:0;top:312px;width:1200px;font-size:52px;color:var(--white);text-align:center}
.hero-title span{color:var(--blue)}
.hero-text{left:350px;top:388px;width:500px;font-size:12.5px;line-height:22px;color:#e8ecf0;text-align:center}
.hero-btn{left:512px;top:462px;width:190px;height:51px;font-size:17px}

/* about */
.about-title{left:163px;top:826px;font-size:32px}
.about-text{left:163px;top:880px;width:332px}
.about-text p+p{margin-top:19px}
.about-btn{left:163px;top:1108px;width:152px;height:40px}

/* services */
.services-panel{left:470px;top:1200px;width:705px;height:675px;background:var(--panel)}
.services-title{left:698px;top:1350px;font-size:30px}
.services-intro{left:698px;top:1413px;width:335px}
.service{position:absolute;left:698px;width:360px;height:75px}
.service .icon{position:absolute;left:0;top:0;width:75px;height:75px;background:var(--white);box-shadow:0 2px 6px rgba(0,0,0,.08);display:flex;align-items:center;justify-content:center}
.service h3{position:absolute;left:95px;top:18px;font-family:"Bungee",Impact,sans-serif;font-weight:400;font-size:14px;color:var(--ink)}
.service p{position:absolute;left:95px;top:40px;width:260px}

/* projects */
.section-title{left:0;width:1200px;text-align:center;font-size:31px}
.section-intro{left:400px;width:400px;text-align:center}
.view-btn{left:550px;top:2556px;width:113px;height:40px}

/* testimonials */
.card{position:absolute;top:2798px;width:435px;height:230px;background:var(--white);box-shadow:0 2px 10px rgba(0,0,0,.10);padding:30px 32px}
.card blockquote{font-style:italic;font-size:12px;line-height:22.5px;color:#555}
.card .name{margin-top:20px;font-family:"Bungee",Impact,sans-serif;font-size:14px;color:var(--ink)}
.card .role{margin-top:6px;font-size:10.5px;color:var(--blue)}
.card .qmark{position:absolute;right:42px;top:0}
.arrow{position:absolute;top:3082px;width:32px;height:30px;border:1px solid #d6d9dd;background:#f4f5f6;display:flex;align-items:center;justify-content:center}

/* contact */
.contact-panel{left:38px;top:3197px;width:780px;height:563px;background:var(--panel)}
.contact-title{left:163px;top:3266px;font-size:31px}
.contact-intro{left:163px;top:3318px;width:420px}
.field{position:absolute;border:1px solid var(--blue);background:var(--white);font-size:10px;color:var(--blue);padding:12px 15px}
.drop-btn{left:163px;top:3623px;width:129px;height:38px}

/* footer */
.footer-brand{left:0;top:3838px;width:1200px;justify-content:center;font-size:36px}
.footer-text{left:400px;top:3932px;width:400px;text-align:center}
.footer-rule{left:163px;top:4002px;width:887px;height:1px;background:var(--line)}
.footer-nav{left:0;top:4032px;width:1200px;justify-content:center}
.social{position:absolute;top:4083px;width:38px;height:36px;border:1px solid var(--blue)}
.social.active{background:var(--blue)}
.copyright-bar{left:38px;top:4198px;width:1137px;height:48px;background:var(--dark);color:#c9ccd0;font-size:10px;display:flex;align-items:center;justify-content:center}
</style>
</head>
<body>

<header>
  <div class="abs top-rule"></div>
  <div class="abs brand header-brand"><span class="mark"></span>BRIXMORVO</div>
  <nav class="abs nav header-nav"><span>Home</span><span>About Us</span><span>Services</span><span>Testimonials</span><span>Gallery</span><span>Contact Us</span></nav>
  <a class="btn quote-btn">REQUEST A QUOTE</a>
</header>

<section class="hero-section">
  <div class="photo hero" role="img" aria-label="Construction workers in hard hats and safety vests looking up at a building under construction"></div>
  <div class="abs hero-shade"></div>
  <h1 class="abs display hero-title">THE HEIGHT, <span>PORT</span></h1>
  <p class="abs hero-text">Lorem Ipsum is simply dummy text of the printing and typesetting industry. Lorem Ipsum has been the industry's standard dummy text ever since the 1500s</p>
  <a class="btn hero-btn">GET IN TOUCH</a>
</section>

<section class="about">
  <h2 class="abs display about-title">ABOUT US</h2>
  <div class="abs small about-text">
    <p>Lorem Ipsum is simply dummy text of the printing and typesetting industry. Lorem Ipsum has been the industry's standard dummy text ever since the 1500s, when an unknown printer took a galley of type and scrambled it to make a type specimen book. It has survived not only five centuries, but also the leap into electronic typesetting, remaining essentially unchanged.</p>
    <p>It was popularised in the 1960s with the release of Letraset sheets containing Lorem Ipsum passages.</p>
  </div>
  <a class="btn about-btn">DISCOVER MORE</a>
  <div class="photo" style="left:618px;top:790px;width:239px;height:236px;background:linear-gradient(180deg,#6a7380,#3c4149 60%,#5a4a3a)" role="img" aria-label="Glass towers under construction with a crane"></div>
  <div class="photo" style="left:875px;top:905px;width:168px;height:121px;background:linear-gradient(180deg,#8a96a6,#5b6470)" role="img" aria-label="High-rise under construction against a grey sky"></div>
  <div class="photo" style="left:698px;top:1042px;width:352px;height:220px;background:linear-gradient(180deg,#9db7cf 0%,#c9a46a 50%,#8a5a38 100%)" role="img" aria-label="Timber-framed house under construction"></div>
</section>

<section class="services">
  <div class="abs services-panel"></div>
  <div class="photo" style="left:38px;top:1316px;width:607px;height:452px;background:linear-gradient(160deg,#2b7d8f 0%,#4f8fa0 40%,#8a6a5a 75%,#3a4a55 100%)" role="img" aria-label="Tower under construction with scaffolding next to a finished high-rise"></div>
  <h2 class="abs display services-title">OUR SERVICES</h2>
  <p class="abs small services-intro">Lorem Ipsum is simply dummy text of the printing and typesetting industry. Lorem Ipsum has been the industry's standard dummy text ever since the 1500s.</p>

  <div class="service" style="top:1494px">
    <div class="icon"><svg width="44" height="40" viewBox="0 0 44 40" fill="none" stroke="#111418" stroke-width="2.2"><rect x="4" y="4" width="36" height="30"/><line x1="4" y1="12" x2="40" y2="12"/><line x1="4" y1="26" x2="40" y2="26"/><line x1="4" y1="12" x2="40" y2="26"/><line x1="40" y1="12" x2="4" y2="26"/><line x1="6" y1="34" x2="6" y2="39" stroke="#0a9de0"/><line x1="38" y1="34" x2="38" y2="39" stroke="#0a9de0"/></svg></div>
    <h3>SCAFFOLDING</h3>
    <p class="small">Lorem Ipsum is simply dummy text of the printing and typesetting industry.</p>
  </div>
  <div class="service" style="top:1600px">
    <div class="icon"><svg width="44" height="40" viewBox="0 0 44 40" fill="none" stroke="#111418" stroke-width="2.2"><rect x="3" y="4" width="38" height="26"/><line x1="22" y1="30" x2="22" y2="36"/><line x1="14" y1="37" x2="30" y2="37"/><path d="M10 24 V14 L18 9 L26 14 V24" stroke="#0a9de0"/><rect x="29" y="12" width="8" height="12" stroke="#0a9de0"/></svg></div>
    <h3>ELEVATION</h3>
    <p class="small">Lorem Ipsum is simply dummy text of the printing and typesetting industry.</p>
  </div>
  <div class="service" style="top:1703px">
    <div class="icon"><svg width="44" height="40" viewBox="0 0 44 40" fill="none" stroke="#111418" stroke-width="2.4"><path d="M4 20 L22 4 L40 20"/><path d="M9 16 V37 H35 V16"/><path d="M22 14 a5 5 0 1 0 0.1 0" stroke="#0a9de0"/><line x1="22" y1="24" x2="22" y2="34" stroke="#0a9de0" stroke-width="3.5"/></svg></div>
    <h3>RENOVATION</h3>
    <p class="small">Lorem Ipsum is simply dummy text of the printing and typesetting industry.</p>
  </div>
</section>

<section class="projects">
  <h2 class="abs display section-title" style="top:1945px">LATEST PROJECTS</h2>
  <p class="abs small section-intro" style="top:2010px">Lorem Ipsum is simply dummy text of the printing and typesetting industry. Lorem Ipsum has been the industry's standard dummy text ever since the 1500s.</p>
  <div class="photo" style="left:163px;top:2074px;width:432px;height:429px;background:linear-gradient(165deg,#2f7f94 0%,#6aa9b8 45%,#2f5a3a 85%)" role="img" aria-label="Glass office tower with trees in the foreground"></div>
  <div class="photo" style="left:618px;top:2074px;width:205px;height:203px;background:linear-gradient(180deg,#6f6252,#a38466,#4e5a3c)" role="img" aria-label="Workers climbing scaffolding"></div>
  <div class="photo" style="left:845px;top:2074px;width:205px;height:203px;background:linear-gradient(180deg,#6d8fc4,#b9a8c2 70%,#c9a9a8)" role="img" aria-label="Steel frame structure against a dusk sky"></div>
  <div class="photo" style="left:618px;top:2300px;width:205px;height:203px;background:linear-gradient(180deg,#c7c9cc,#8a6548 60%,#5a3e2a)" role="img" aria-label="Rows of scaffolding frames"></div>
  <div class="photo" style="left:845px;top:2300px;width:205px;height:203px;background:linear-gradient(180deg,#d8dadc,#3d4650 40%,#2a3038)" role="img" aria-label="Residential tower with balconies"></div>
  <a class="btn view-btn">VIEW MORE</a>
</section>

<section class="testimonials">
  <h2 class="abs display section-title" style="top:2674px">OUR TESTIMONIALS</h2>
  <p class="abs small section-intro" style="top:2739px">Lorem Ipsum is simply dummy text of the printing and typesetting industry. Lorem Ipsum has been the industry's standard dummy text ever since the 1500s.</p>

  <article class="card" style="left:162px">
    <svg class="qmark" width="26" height="22" viewBox="0 0 26 22"><path d="M0 0 H10 V12 L6 22 H2 L4 12 H0 Z M14 0 H24 V12 L20 22 H16 L18 12 H14 Z" fill="#0a9de0"/></svg>
    <blockquote>" Lorem Ipsum is simply dummy text of the printing and typesetting industry. Lorem Ipsum has been the industry's standard dummy text ever since the 1500s, when an unknown printer took a galley of type and scrambled it to make a type specimen book.</blockquote>
    <div class="name">CLIENT NAME</div>
    <div class="role">Elevation Worker</div>
  </article>
  <article class="card" style="left:617px">
    <svg class="qmark" width="26" height="22" viewBox="0 0 26 22"><path d="M0 0 H10 V12 L6 22 H2 L4 12 H0 Z M14 0 H24 V12 L20 22 H16 L18 12 H14 Z" fill="#0a9de0"/></svg>
    <blockquote>" Lorem Ipsum is simply dummy text of the printing and typesetting industry. Lorem Ipsum has been the industry's standard dummy text ever since the 1500s, when an unknown printer took a galley of type and scrambled it to make a type specimen book.</blockquote>
    <div class="name">CLIENT NAME</div>
    <div class="role">Elevation Worker</div>
  </article>
  <div class="arrow" style="left:572px"><svg width="8" height="12" viewBox="0 0 8 12" fill="none" stroke="#777" stroke-width="1.5"><path d="M6 1 L1 6 L6 11"/></svg></div>
  <div class="arrow" style="left:608px"><svg width="8" height="12" viewBox="0 0 8 12" fill="none" stroke="#777" stroke-width="1.5"><path d="M2 1 L7 6 L2 11"/></svg></div>
</section>

<section class="contact">
  <div class="abs contact-panel"></div>
  <h2 class="abs display contact-title">CONTACT US</h2>
  <p class="abs small contact-intro">Lorem Ipsum is simply dummy text of the printing and typesetting industry. Lorem Ipsum has been the industry's standard dummy text ever since the 1500s.</p>
  <div class="field" style="left:163px;top:3385px;width:204px;height:40px">Name:</div>
  <div class="field" style="left:383px;top:3385px;width:204px;height:40px">Phone:</div>
  <div class="field" style="left:163px;top:3438px;width:424px;height:40px">Email:</div>
  <div class="field" style="left:163px;top:3491px;width:424px;height:72px">Message:</div>
  <a class="btn drop-btn">DROP A LINE</a>
  <div class="photo" style="left:642px;top:3253px;width:453px;height:449px;background:linear-gradient(150deg,#c9ccd2 0%,#6f88b8 40%,#b8323e 75%,#8a2430 100%)" role="img" aria-label="Two construction workers in hard hats reviewing plans"></div>
</section>

<footer>
  <div class="abs brand footer-brand"><span class="mark" style="width:20px;height:20px"></span>BRIXMORVO</div>
  <p class="abs small footer-text">Lorem Ipsum is simply dummy text of the printing and typesetting industry. Lorem Ipsum has been the industry's standard dummy text ever since the 1500s.</p>
  <div class="abs footer-rule"></div>
  <nav class="abs nav footer-nav"><span>Home</span><span>About Us</span><span>Services</span><span>Testimonials</span><span>Gallery</span><span>Contact Us</span></nav>
  <div class="social" style="left:520px"></div>
  <div class="social active" style="left:565px"></div>
  <div class="social" style="left:610px"></div>
  <div class="social" style="left:655px"></div>
  <div class="abs copyright-bar">Copyright © 2020 Brixmorvo. All Rights Reserved. Terms &amp; Conditions | Privacy Policy</div>
</footer>

</body>
</html>
```